We need a new letterhead design for a 20 year old consulting company. Ideally jpg (or other) image that can be dropped onto a word/publisher document. Currently we have a 'design' header and 'detail' footer (with address etc), and this works well, but is not essential. The letterhead/footer must be suitable for portrait and landscape (or 2 separate images to cater for both alignments) and must be suitable for in-office printing (ie doesn't lose content outside of printer margins)

Our business card includes a cutout jigsaw piece, so it is essential that a jigsaw image is included in the design. Our most recent design also included clouds, but I'm over this. Use SUBDUED greyish/blue colouring.

I've attached the old letterhead (file names letterhead fat and letterhead master), and one I've mocked up (TRWB letterhead Nov 12) and market tested (new name is TRWB Strategy), so this should provide a starting point. NOTE COMPANY NAME IS TRWB Strategy - quite a few designs have come in with our old company name.

The design needs to communicate simplicity, experience, ideas. our tagline is "clarity and direction", but we also use "when you need ideas". Don't include these in the design, we change them quite often.

Many thanks

Delphine

Hi Designers

thanks for the first suite of designs. Having seen them, I need to be a little more specific about some things:

We are no longer using "Lanternfield Partners", the logo is TRWB Strategy (preferably with the word 'strategy' underneath TRWB and the same size

I don't like watermarks (sorry), so I'm ignoring those, and if I like a design it will have all watermarks removed.

I like the 'swoop' that we have been using - I'm not stuck on it, but like the designs with a bit more creativity better

I don't like boxes of text (could do that myself on a word processor), it needs to look like it's been designed by a graphic designer

Please keep the colours blue/grey (as per my TRWB Strategy attachment)

Cheers

Delphine

Hello again

I use the letterhead for report covers, so the image at the header and footer need to frame the page - designs that just use text at the top or bottom won't work because they won't 'stand out' when used as a cover.

Thanks

K

Hi designers, some lovely work coming through. Pls don't forget that I'm after a letterhead that I'll be printing on ink and laser printers, So anything close to the edge of the paper (eg address) won't print. It will be necessary for the design to work within printable range.

Ta

K

Reason: Hi everyone Because of the Christmas Holidays, I have decided to extend the deadline by 2 weeks. Cheers Delphine

corporate and government clients, CEOs etc

• Blue/grey colours
Jigsaw logo
Suitable for portrait and landscape
name: TRWB Strategy
• Fresh and contemporary
• the old company name (TRWB Lanternfield Partners)
important content (design/contact details) that will not print on ink/laser printer

```html
<!DOCTYPE html>
<html lang="en">
<head>
<meta charset="utf-8">
<title>TRWB Strategy Letterhead</title>
<link rel="stylesheet" href="https://fonts.googleapis.com/css2?family=Arimo:wght@400;700&family=Libre+Baskerville&family=Great+Vibes&display=swap">
<style>
  :root {
    --brand-blue: #174a80;
    --canvas-grey: #ebebeb;
    --paper: #ffffff;
    --body-ink: #454545;
    --heading-ink: #2e2e2e;
    --on-brand: #ffffff;
    --brand-tint: #b9c3d6;
  }
  * { box-sizing: border-box; margin: 0; padding: 0; }
  html, body {
    width: 1200px;
    height: 910px;
    overflow: hidden;
    background: var(--canvas-grey);
  }
  .letterhead {
    position: absolute;
    left: 295px;
    top: 25px;
    width: 610px;
    height: 860px;
    background: var(--paper);
    border: 1px solid #d6d6d6;
    font-family: "Arimo", Arial, sans-serif;
    color: var(--body-ink);
  }
  .masthead {
    position: absolute;
    left: 0; top: 0;
    width: 100%;
    height: 117px;
    background: var(--brand-blue);
    color: var(--on-brand);
  }
  .masthead-brand {
    position: absolute;
    left: 40px;
    top: 36px;
    display: flex;
    align-items: center;
    gap: 16px;
  }
  .brand-lockup {
    display: flex;
    flex-direction: column;
    font-family: "Libre Baskerville", Georgia, serif;
    color: var(--on-brand);
  }
  .brand-name {
    font-size: 34px;
    line-height: 1;
  }
  .brand-descriptor {
    font-size: 16px;
    line-height: 1;
    letter-spacing: 2.6px;
    margin-top: 8px;
  }
  .brand-square {
    width: 22px; height: 22px;
    background: var(--on-brand);
    align-self: flex-start;
    margin-top: 4px;
  }
  .contact-block {
    position: absolute;
    left: 458px;
    top: 22px;
    font-size: 14px;
    line-height: 17px;
    font-style: normal;
  }
  .contact-line { display: flex; align-items: center; gap: 6px; font-size: 13px; }
  .contact-line svg { width: 11px; height: 11px; fill: var(--on-brand); }
  .letter-body {
    position: absolute;
    left: 37px;
    top: 198px;
    width: 552px;
    font-size: 12.1px;
    line-height: 20.5px;
  }
  .salutation {
    font-weight: 700;
    color: var(--heading-ink);
    margin-bottom: 20px;
  }
  .letter-body p.paragraph { margin-bottom: 20.5px; }
  .signature {
    font-family: "Great Vibes", cursive;
    font-size: 28px;
    color: var(--heading-ink);
    margin-top: 8px;
    margin-left: 4px;
  }
  .website {
    position: absolute;
    left: 32px;
    top: 826px;
    font-size: 14px;
    color: var(--brand-blue);
  }
  .footer-brand {
    position: absolute;
    left: 398px;
    top: 792px;
    display: flex;
    align-items: center;
    gap: 14px;
  }
  .footer-brand .brand-lockup { color: var(--brand-blue); }
  .footer-brand .brand-name { font-size: 30px; }
  .footer-brand .brand-descriptor { font-size: 13px; letter-spacing: 2.4px; margin-top: 6px; }
  .footer-brand .brand-square { background: var(--brand-tint); width: 30px; height: 30px; margin-top: 0; align-self: center; }
</style>
</head>
<body>
  <main class="letterhead">
    <header class="masthead">
      <div class="masthead-brand">
        <div class="brand-lockup">
          <span class="brand-name">TRWB</span>
          <span class="brand-descriptor">Strategy</span>
        </div>
        <span class="brand-square"></span>
      </div>
      <address class="contact-block">
        <div>14 Harlow Lane</div>
        <div>Westbrook SA 5099</div>
        <div class="contact-line">
          <svg viewBox="0 0 24 24"><path d="M3 8c0-3 5-5 9-5s9 2 9 5v2h-5V8H8v2H3zM6 11h12l3 9H3z"/></svg>
          <span>(+618) 8000 3172</span>
        </div>
        <div class="contact-line">
          <svg viewBox="0 0 24 24"><path d="M2 5h20v14H2zM4 7v1l8 5 8-5V7l-8 5z"/></svg>
          <span>info@trwb.com.au</span>
        </div>
      </address>
    </header>

    <section class="letter-body">
      <p class="salutation">Dear Customer,</p>
      <p class="paragraph">Lorem ipsum dolor sit amet, consectetur adipiscing elit. Donec elementum velit sit amet libero fringilla adipiscing. Aliquam sollicitudin, leo vitae molestie facilisis, tellus ligula varius velit, vitae tincidunt lacus purus vitae nulla. Nulla imperdiet, odio quis ultrices ornare, diam est dictum lacus, et vehicula est magna at metus. Integer mattis lorem quis tortor accumsan ultrices ac ut massa. Duis eget metus ut risus scelerisque ornare quis eget dui. Aliquam lobortis dolor vitae magna volutpat eu facilisis tellus molestie. Sed a purus quis nibh lacinia interdum ut at leo.</p>
      <p class="paragraph">Integer consequat velit quis elit hendrerit imperdiet. Donec felis velit, volutpat vel convallis nec, sollicitudin et nulla. Pellentesque sodales elementum aliquam. Donec convallis, turpis sit amet laoreet ultricies, enim est elementum magna, dictum lobortis eros tellus quis diam. Nunc suscipit augue non nisl volutpat volutpat. Ut egestas ultrices purus, eget varius nibh placerat in. Cras leo ante, congue id ultricies a, ornare eu est. Curabitur eleifend tincidunt mi eget tristique.</p>
      <p class="paragraph">Etiam arcu augue, ornare vitae consectetur luctus, tincidunt vitae urna. Lorem ipsum dolor sit amet, consectetur adipiscing elit. Donec vitae tortor quis orci adipiscing lobortis. Morbi aliquet orci quis mi viverra sollicitudin. Sed eget pellentesque turpis. Aliquam commodo sodales ultrices. Nullam ut elit vitae elit suscipit porttitor viverra non mi. Donec diam mi, tincidunt nec sodales vestibulum, iaculis a urna. Nulla facilisi. Integer consequat velit quis elit hendrerit imperdiet.</p>
      <p class="sign-off">Your Sincerelly</p>
      <p class="signature">Signature</p>
    </section>

    <footer>
      <div class="website">www.trwb.com.au</div>
      <div class="footer-brand">
        <div class="brand-lockup">
          <span class="brand-name">TRWB</span>
          <span class="brand-descriptor">Strategy</span>
        </div>
        <span class="brand-square"></span>
      </div>
    </footer>
  </main>
</body>
</html>
```